www.HelenTrobbitt.com

I am looking to redesign my author website. I want it to reflect my personality but look more professional AND more marketing savvy.

I am looking for:
- a header/banner with JUST MY NAME:
Helen Trobbitt

- a header/banner using my name and log line - like this:
Helen Trobbitt
Professional Writer. Amateur Mom.

- And a logo using my name and a different log line:
Helen Trobbitt
Finding the funny in parenthood before somebody loses an eye.

- social media buttons for Chatterleaf, Quorvel, Pictolane, clipwardly, Vexaro +.

Regarding the design style I want to use the attached design for the basis of the website. I would like to use the logo in the UPPER RIGHT HAND CORNER of the four designs attached. It is the design with the slate blue background and yellowish/orangish colors.

I LOVE the typewriter font and would like to use that for my column headers - ideally, I would love it if when you roll over the headers it looks like they are being typed out - but I don't know if that is possible. If it isn't, happy just just get the headers in that font.

Target Market(s)

30-50 year old parents and educators. My target audience is educated with a great sense of style and sense of humor.

Industry/Entity Type

Marketing

Requirements
Must have
• - Clear, bold, client friendly design/buttons
- Professional, web-savvy design
- Modern/RETRO look
- Headers for the following verticals:
About Me
Books
Articles
TV
Hire Me
Speaking
Consulting
Classes
School Visits
Press
Blaaaahhhhg! (Blog)
Contact Me

```html
<!DOCTYPE html>
<html lang="en">
<head>
<meta charset="utf-8">
<title>Helen Trobbitt – Name Banners</title>
<link rel="stylesheet" href="https://fonts.googleapis.com/css2?family=Oswald:wght@600&family=Grand+Hotel&family=Special+Elite&family=Arvo&family=Stardos+Stencil:wght@700&display=swap">
<style>
  :root {
    --page-bg: #ffffff;
    --ink-dark: #4a4a4a;
    --slate: #8fa3ae;
    --slate-edge: #7d919c;
    --slate-light: #a4b5be;
    --apricot: #f9c57c;
    --apricot-edge: #e8b066;
    --apricot-light: #fbd49c;
    --apricot-text: #f7c073;
    --slate-text: #8d9ea8;
    --ornament: #ffffff;
  }
  * { margin: 0; padding: 0; box-sizing: border-box; }
  html, body { width: 1200px; height: 900px; overflow: hidden; background: var(--page-bg); }
  .sheet { position: relative; width: 1200px; height: 900px; }
  .sheet-title {
    position: absolute; left: 69px; top: 12px;
    font: 600 30px/1.2 "Oswald", sans-serif; color: var(--ink-dark);
  }
  .banner { position: absolute; left: 66px; width: 602px; height: 144px; }
  .banner svg { position: absolute; inset: 0; }
  .banner--one { top: 74px; }
  .banner--two { top: 290px; }
  .banner--three { top: 508px; }
  .banner--four { top: 714px; }
  .banner-name {
    position: absolute; left: 0; top: 0; width: 566px; height: 144px;
    display: flex; align-items: center; justify-content: center;
    white-space: nowrap;
  }
  .ornament {
    position: absolute; left: 260px; width: 46px; height: 16px;
    background: var(--ornament); opacity: .85; border-radius: 8px;
  }
  .ornament--top { top: 8px; }
  .ornament--bottom { bottom: 10px; }
  .name-cursive { font: 68px "Grand Hotel", cursive; color: var(--apricot-text); }
  .name-typewriter { font: 46px "Special Elite", monospace; color: var(--slate-text); }
  .name-slab { font: 52px "Arvo", serif; color: var(--apricot-text); }
  .name-stencil { font: 700 48px "Stardos Stencil", sans-serif; color: var(--slate-text); letter-spacing: 1px; }
  .style-label {
    position: absolute; left: 694px;
    font: 600 26px/1 "Oswald", sans-serif; color: var(--ink-dark);
  }
  .style-label--one { top: 132px; }
  .style-label--two { top: 346px; }
  .style-label--three { top: 554px; }
  .style-label--four { top: 770px; }
</style>
</head>
<body>
<main class="sheet">
  <h1 class="sheet-title">Banner with name</h1>

  <div class="banner banner--one">
    <svg width="602" height="144" viewBox="0 0 602 144" aria-hidden="true">
      <polygon points="0,0 602,0 534,72 602,144 0,144" fill="var(--slate)"/>
      <polygon points="0,0 602,0 599,3 0,3" fill="var(--slate-light)"/>
      <polygon points="0,140 598,140 602,144 0,144" fill="var(--slate-edge)"/>
    </svg>
    <span class="ornament ornament--top" role="img" aria-label="Small white flourish ornament"></span>
    <p class="banner-name name-cursive">Helen Trobbitt</p>
    <span class="ornament ornament--bottom" role="img" aria-label="Small white flourish ornament"></span>
  </div>
  <p class="style-label style-label--one">Cursive Font</p>

  <div class="banner banner--two">
    <svg width="602" height="144" viewBox="0 0 602 144" aria-hidden="true">
      <polygon points="0,0 602,0 534,72 602,144 0,144" fill="var(--apricot)"/>
      <polygon points="0,0 602,0 599,3 0,3" fill="var(--apricot-light)"/>
      <polygon points="0,140 598,140 602,144 0,144" fill="var(--apricot-edge)"/>
    </svg>
    <span class="ornament ornament--top" role="img" aria-label="Small white flourish ornament"></span>
    <p class="banner-name name-typewriter">Helen Trobbitt</p>
    <span class="ornament ornament--bottom" role="img" aria-label="Small white flourish ornament"></span>
  </div>
  <p class="style-label style-label--two">Type Writter Font - 1</p>

  <div class="banner banner--three">
    <svg width="602" height="144" viewBox="0 0 602 144" aria-hidden="true">
      <polygon points="0,0 602,0 534,72 602,144 0,144" fill="var(--slate)"/>
      <polygon points="0,0 602,0 599,3 0,3" fill="var(--slate-light)"/>
      <polygon points="0,140 598,140 602,144 0,144" fill="var(--slate-edge)"/>
    </svg>
    <span class="ornament ornament--top" role="img" aria-label="Small white flourish ornament"></span>
    <p class="banner-name name-slab">Helen Trobbitt</p>
    <span class="ornament ornament--bottom" role="img" aria-label="Small white flourish ornament"></span>
  </div>
  <p class="style-label style-label--three">Type Writter Font - 2</p>

  <div class="banner banner--four">
    <svg width="602" height="144" viewBox="0 0 602 144" aria-hidden="true">
      <polygon points="0,0 602,0 534,72 602,144 0,144" fill="var(--apricot)"/>
      <polygon points="0,0 602,0 599,3 0,3" fill="var(--apricot-light)"/>
      <polygon points="0,140 598,140 602,144 0,144" fill="var(--apricot-edge)"/>
    </svg>
    <span class="ornament ornament--top" role="img" aria-label="Small white flourish ornament"></span>
    <p class="banner-name name-stencil">HELEN TROBBITT</p>
    <span class="ornament ornament--bottom" role="img" aria-label="Small white flourish ornament"></span>
  </div>
  <p class="style-label style-label--four">Stencil Font</p>
</main>
</body>
</html>
```